Business Card Design using new attached logo

We are a family run Plumbing and Heating firm looking to improve our company image with an improved business card and new logo.We are looking to keep the company colour (Blue) involved in our design

Reason: New logo added which needs to be incorporated on designs

Industry/Entity Type

Business

Contact Information for Business Card

See attachment of all info required.

Requirements
Must have
• We have just picked a new company logo which is attached.
• Could you please provide your business card designs using this logo.
• We are looking for the logo on the back as well as the front with all the info required

```html
<!DOCTYPE html>
<html lang="en">
<head>
<meta charset="utf-8">
<title>Kestrel Services Ltd – Business Card</title>
<link href="https://fonts.googleapis.com/css2?family=Ubuntu:wght@500;700&display=swap" rel="stylesheet">
<style>
  :root {
    --backdrop: #e7e4df;
    --card: #ffffff;
    --navy: #1f2a5c;
    --blue: #0f5aa8;
    --red: #e2231f;
    --purple-soft: #e9dcec;
    --sky: #2f9be0;
    --shadow: rgba(0, 0, 0, 0.28);
  }
  * { margin: 0; padding: 0; box-sizing: border-box; }
  html, body {
    width: 1200px;
    height: 1200px;
    overflow: hidden;
    background: var(--backdrop);
    font-family: "Ubuntu", Arial, sans-serif;
  }
  .card {
    position: absolute;
    left: 160px;
    width: 840px;
    height: 552px;
    background: var(--card);
    box-shadow: 0 6px 18px var(--shadow);
    overflow: hidden;
  }
  .card--front { top: 30px; }
  .card--back { top: 604px; }

  .brand {
    position: absolute;
    left: 0;
    width: 840px;
    display: flex;
    flex-direction: column;
    align-items: center;
  }
  .brand__row { display: flex; align-items: center; gap: 16px; }
  .brand__dot { border-radius: 50%; background: var(--sky); }
  .brand__name {
    color: var(--navy);
    font-weight: 700;
    text-transform: uppercase;
    letter-spacing: 0.5px;
    white-space: nowrap;
  }
  .brand__tagline {
    color: var(--red);
    font-weight: 500;
    text-transform: uppercase;
    letter-spacing: 3px;
  }
  .card--front .brand { top: 222px; }
  .card--front .brand__dot { width: 34px; height: 34px; }
  .card--front .brand__name { font-size: 46px; }
  .card--front .brand__tagline { font-size: 18px; margin-top: 8px; }

  .card--back .brand { top: 292px; left: -10px; }
  .card--back .brand__dot { width: 28px; height: 28px; }
  .card--back .brand__name { font-size: 36px; }
  .card--back .brand__tagline { font-size: 15px; margin-top: 6px; }

  .rule-thin {
    position: absolute;
    left: 0; top: 354px;
    width: 100%; height: 6px;
    background: var(--blue);
  }
  .contact-band {
    position: absolute;
    left: 0; top: 366px;
    width: 100%; height: 126px;
    background: var(--blue);
    color: #fff;
    font-weight: 700;
  }
  .contact { position: absolute; top: 24px; }
  .contact--phone { left: 52px; }
  .contact--fax { left: 552px; }
  .contact__label { font-size: 31px; letter-spacing: 0.5px; }
  .contact__value { font-size: 31px; margin-top: 8px; letter-spacing: 0.5px; }
  .address-band {
    position: absolute;
    left: 0; top: 504px;
    width: 100%; height: 48px;
    background: var(--red);
    color: #fff;
    font-size: 22px;
    font-weight: 500;
    line-height: 48px;
    padding-left: 42px;
    letter-spacing: 0.3px;
    white-space: nowrap;
  }
  .pipework-area {
    position: absolute;
    inset: 0;
    background: radial-gradient(ellipse at center, var(--card) 45%, var(--purple-soft) 100%);
  }
</style>
</head>
<body>
  <section class="card card--front">
    <div class="brand">
      <div class="brand__row">
        <span class="brand__dot"></span>
        <span class="brand__name">Kestrel Services Ltd</span>
      </div>
      <div class="brand__tagline">Plumbing and Heating</div>
    </div>
    <div class="rule-thin"></div>
    <div class="contact-band">
      <div class="contact contact--phone">
        <div class="contact__label">PHONE</div>
        <div class="contact__value">020 7946 0321</div>
      </div>
      <div class="contact contact--fax">
        <div class="contact__label">FAX</div>
        <div class="contact__value">020 7946 0187</div>
      </div>
    </div>
    <div class="address-band">14 HARBOUR PARADE, FENWICK ROAD, ASHFORD, KENT TN9 2QX</div>
  </section>

  <section class="card card--back">
    <div class="pipework-area" role="img" aria-label="Decorative purple pipework running along the left and right edges of the card"></div>
    <div class="brand">
      <div class="brand__row">
        <span class="brand__dot"></span>
        <span class="brand__name">Kestrel Services Ltd</span>
      </div>
      <div class="brand__tagline">Plumbing and Heating</div>
    </div>
  </section>
</body>
</html>
```